Brightwater Contracting-work at height professionals

Specializing In:
Summit Line Window Washing
Interior atrium maintenance
Dryer vent cleaning
Building maintenance/inspection
Property maintenance
Pressure washing

Portray:experienced team, QUILN certified technicians,

Needs to portray the rope access industry and window washing via rope access (not bosun chair!)

Pictures are just examples only of our work

Designs are looking good! Check the brief again. I updated it

Please change “hi-rise to”Summit Line” Thanks, and check rest of the brief for updates on spelling and wording Thanks, designs are looking good!

Aswell need a company logo with the designs Thanks

Target Market(s)

Summit Line property management companies

Industry/Entity Type

Property Maintenance

Contact Information for Business Card

Torvin Maddock
Brightwater Contracting
Work at height professionals
C:555-201-3387
E:torvin@brightwatercontracting.co
E:sales@brightwatercontracting.co
Serving southern Alberta

Font styles to use
Sans Serif

Colors

Requirements
Must have
• Summit Line Window Washing
• Dryer Vent Cleaning
• Snow Management
• Interior Atriums Maintenance
• Property Maintenance
• QUILN Certified
Nice to have
• Work at Height Professionals
• Care for every level of your building
• A company logo
• Downtown Calgary Alberta background
Should not have
• Bosun chairs
• Hi-rise

```html
<!DOCTYPE html>
<html lang="en">
<head>
<meta charset="utf-8">
<title>Summit Line – Business Card</title>
<link rel="stylesheet" href="https://fonts.googleapis.com/css2?family=Open+Sans:wght@700&display=swap">
<style>
  :root {
    --backdrop: #e4e4e6;
    --card-navy: #30324a;
    --card-navy-light: #3a3d57;
    --card-navy-deep: #2b2d43;
    --mullion: #23222f;
    --name-white: #ffffff;
    --tagline-white: #ffffff;
    --figure-yellow: #f2c23a;
    --figure-amber: #e0a83a;
    --figure-slate: #3f5670;
  }
  * { margin: 0; padding: 0; box-sizing: border-box; }
  html, body {
    width: 1200px;
    height: 900px;
    overflow: hidden;
    background: var(--backdrop);
  }
  .stage {
    width: 1200px;
    height: 900px;
    display: flex;
    align-items: center;
    justify-content: center;
  }
  .business-card {
    position: relative;
    width: 1000px;
    height: 572px;
    overflow: hidden;
    background: linear-gradient(135deg, var(--card-navy-light) 0%, var(--card-navy) 55%, var(--card-navy-deep) 100%);
    box-shadow: 0 18px 40px rgba(0,0,0,0.28);
  }
  .window-grid {
    position: absolute;
    inset: 0;
    width: 100%;
    height: 100%;
  }
  .rope-tech-illustration {
    position: absolute;
    left: 40px;
    top: 70px;
    width: 210px;
    height: 440px;
    border-radius: 8px;
    background: linear-gradient(180deg, var(--figure-yellow) 0%, var(--figure-amber) 45%, var(--figure-slate) 100%);
    opacity: 0.9;
  }
  .brand-block {
    position: absolute;
    left: 280px;
    top: 185px;
    width: 690px;
  }
  .brand-name {
    display: flex;
    align-items: center;
    gap: 20px;
    font-family: "Open Sans", sans-serif;
    font-weight: 700;
    font-size: 92px;
    line-height: 1.1;
    color: var(--name-white);
    white-space: nowrap;
  }
  .brand-mark {
    flex: none;
    width: 34px;
    height: 34px;
    background: var(--name-white);
  }
  .brand-tagline {
    margin-top: 16px;
    font-family: "Open Sans", sans-serif;
    font-weight: 700;
    font-size: 27px;
    letter-spacing: 0.5px;
    color: var(--tagline-white);
    white-space: nowrap;
  }
</style>
</head>
<body>
  <main class="stage">
    <section class="business-card">
      <svg class="window-grid" viewBox="0 0 1000 572" preserveAspectRatio="none" aria-hidden="true">
        <g fill="var(--mullion)">
          <rect x="222" y="0" width="22" height="572"/>
          <rect x="520" y="0" width="22" height="572"/>
          <rect x="800" y="0" width="22" height="572"/>
          <rect x="0" y="96" width="1000" height="20"/>
          <rect x="0" y="470" width="1000" height="22"/>
        </g>
      </svg>
      <div class="rope-tech-illustration" role="img" aria-label="Illustration of a rope access technician in helmet and harness washing a window with a squeegee"></div>
      <div class="brand-block">
        <div class="brand-name"><span class="brand-mark"></span>Summit Line</div>
        <p class="brand-tagline">Care for every level of your building</p>
      </div>
    </section>
  </main>
</body>
</html>
```